Stationery Design Project

Please create a custom Stationery Design for Brookvale Homes. The logo is attached to this brief.

Please Include:
- Letterhead
- With Compliments slip
- Envelope

Please also see open Business Card project: http://briefs.gridmarket-example.com/task.aspx?id=571209

Industry/Entity Type

Business

```html
<!DOCTYPE html>
<html lang="en">
<head>
<meta charset="utf-8">
<title>Brookvale Homes – Stationery</title>
<link href="https://fonts.googleapis.com/css2?family=PT+Sans:wght@400;700&display=swap" rel="stylesheet">
<style>
  :root{
    --backdrop:#5e5e5e;
    --paper:#ffffff;
    --brand-blue:#0a6fc2;
    --brand-green:#8cc63f;
    --brand-yellow:#f5c400;
    --ink:#3a3a3a;
    --ghost:#e4e4e4;
    --rule:#c9c9c9;
  }
  *{box-sizing:border-box;margin:0;padding:0}
  html,body{width:1200px;height:640px;overflow:hidden;background:var(--backdrop)}
  body{position:relative;font-family:"PT Sans",Arial,sans-serif;color:var(--ink)}
  .sheet{position:absolute;background:var(--paper);box-shadow:2px 3px 6px rgba(0,0,0,.45);overflow:hidden}
  .letterhead{left:70px;top:60px;width:384px;height:536px}
  .envelope-front{left:530px;top:31px;width:448px;height:178px}
  .envelope-back{left:724px;top:230px;width:446px;height:179px}
  .comp-slip{left:582px;top:438px;width:343px;height:152px}

  .brand{position:absolute;display:flex;align-items:center;gap:6px;
    color:var(--brand-blue);font-weight:700;white-space:nowrap;letter-spacing:.3px}
  .brand-dot{width:11px;height:11px;border-radius:50%;background:var(--brand-yellow);flex:none}
  .letterhead .brand{left:58px;top:52px;font-size:16px}
  .envelope-front .brand{left:26px;top:38px;font-size:15px}
  .comp-slip .brand{left:24px;top:30px;font-size:13px}
  .envelope-back .brand{left:50%;top:26px;transform:translateX(-50%);font-size:12px}

  .contact{position:absolute;font-size:5.6px;line-height:1.55;color:var(--ink)}
  .contact-row{display:flex;align-items:center;gap:3px}
  .icon{width:6px;height:6px;border-radius:1px;background:var(--brand-blue);flex:none}
  .letterhead .contact{left:274px;top:52px;padding-left:4px;border-left:1px solid var(--rule)}
  .envelope-front .contact{left:26px;top:76px;font-size:5.8px}
  .comp-slip .contact{left:24px;top:66px;font-size:5.4px}
  .address{margin-top:2px}

  .ghost-mark{position:absolute;border-radius:50%;background:var(--ghost)}
  .letterhead .ghost-mark{left:132px;top:210px;width:140px;height:140px}
  .envelope-front .ghost-mark{left:332px;top:52px;width:96px;height:96px}

  .compliments{position:absolute;left:218px;top:12px;font-size:13px;color:var(--brand-blue)}

  .flap{position:absolute;left:0;top:0;width:100%;height:52px}
  .bands{position:absolute;left:0;bottom:0;width:100%;height:20px;display:block}
  .band-green{fill:var(--brand-green)}
  .band-blue{fill:var(--brand-blue)}
</style>
</head>
<body>

<section class="sheet letterhead" aria-label="Letterhead">
  <div class="brand"><span class="brand-dot"></span>Brookvale Homes</div>
  <div class="contact">
    <div class="contact-row"><span class="icon"></span>020 7946 0123</div>
    <div class="contact-row"><span class="icon"></span>www.brookvalehomes.example</div>
    <div class="address">12 Larkfield House, Address Line<br>Ashcombe Business Park, City Name</div>
  </div>
  <div class="ghost-mark" aria-hidden="true"></div>
  <svg class="bands" viewBox="0 0 384 20" preserveAspectRatio="none" aria-hidden="true">
    <polygon class="band-green" points="0,8 222,8 217,20 0,20"/>
    <path class="band-blue" d="M226,20 L232,5 Q234,1 240,1 L384,1 L384,20 Z"/>
  </svg>
</section>

<section class="sheet envelope-front" aria-label="Envelope front">
  <div class="brand"><span class="brand-dot"></span>Brookvale Homes</div>
  <div class="contact">
    <div>12 Larkfield House, Address Line</div>
    <div>Ashcombe Business Park, City Name</div>
  </div>
  <div class="ghost-mark" aria-hidden="true"></div>
  <svg class="bands" viewBox="0 0 448 20" preserveAspectRatio="none" aria-hidden="true">
    <polygon class="band-green" points="0,8 260,8 255,20 0,20"/>
    <path class="band-blue" d="M264,20 L270,5 Q272,1 278,1 L448,1 L448,20 Z"/>
  </svg>
</section>

<section class="sheet envelope-back" aria-label="Envelope back">
  <svg class="flap" viewBox="0 0 446 52" preserveAspectRatio="none" aria-hidden="true">
    <path d="M0,0 Q4,48 40,48 L406,48 Q442,48 446,0" fill="none" stroke="#a9a9a9" stroke-width="1"/>
  </svg>
  <div class="brand">Brookvale Homes</div>
</section>

<section class="sheet comp-slip" aria-label="With compliments slip">
  <div class="brand"><span class="brand-dot"></span>Brookvale Homes</div>
  <div class="compliments">With Compliments</div>
  <div class="contact">
    <div class="contact-row"><span class="icon"></span>020 7946 0123</div>
    <div class="contact-row"><span class="icon"></span>www.brookvalehomes.example</div>
    <div class="address">12 Larkfield House, Address Line<br>Ashcombe Business Park, City Name</div>
  </div>
  <svg class="bands" viewBox="0 0 343 20" preserveAspectRatio="none" aria-hidden="true">
    <polygon class="band-green" points="0,9 199,9 194,20 0,20"/>
    <path class="band-blue" d="M203,20 L209,5 Q211,1 217,1 L343,1 L343,20 Z"/>
  </svg>
</section>

</body>
</html>
```